Corvane Electronics, Inc. Business card

Incorporate a globe.
We repair electronics, sell electronic parts, and we recycle electronics. We've been in business since 1982. A technology feel to the card is preferred. I want to be able to give this card to a client from different industries and make it relate-able. I don't have a logo that I've been partial to in the past. It is not necessary in this case.

Target Market(s)

Consumer, Industrial, Business, Medical

Industry/Entity Type

Business

Contact Information for Business Card

4518 Maple Crest Blvd. Fairhaven, TX 75098
214-555-0187 main 214-555-0143 fax
Paul Bredesen VP

Font styles to use
Serif

Requirements
Must have
• Technology feel
Nice to have
• Metallic look
Should not have
• no pastel colors

```html
<!DOCTYPE html>
<html lang="en">
<head>
<meta charset="utf-8">
<title>Corvane Electronics, Inc. – Business Card</title>
<link rel="stylesheet" href="https://fonts.googleapis.com/css2?family=Roboto:wght@400;500;700;900&display=swap">
<style>
  :root {
    --stage: #e9e6e3;
    --paper: #ffffff;
    --brand-red: #ec1c24;
    --ink-black: #231f20;
    --text-light: #ffffff;
    --card-shadow: rgba(0,0,0,0.18);
  }
  html, body {
    margin: 0;
    width: 1200px;
    height: 900px;
    overflow: hidden;
    background: var(--stage);
    font-family: "Roboto", Arial, sans-serif;
  }
  .canvas { position: relative; width: 1200px; height: 900px; }
  .card {
    position: absolute;
    overflow: hidden;
    box-shadow: 0 4px 14px var(--card-shadow);
  }
  .card--front {
    left: 78px; top: 35px; width: 588px; height: 363px;
    background: var(--paper);
  }
  .card--back {
    left: 388px; top: 505px; width: 567px; height: 352px;
    background: var(--ink-black);
  }
  .card__bands { position: absolute; inset: 0; }
  .wordmark {
    position: absolute;
    left: 0; right: 0;
    color: var(--brand-red);
    font-weight: 900;
    text-align: center;
    line-height: 1;
  }
  .wordmark__name { display: block; font-size: 76px; letter-spacing: -2px; }
  .wordmark__suffix { display: block; font-size: 17px; letter-spacing: 3px; margin-top: 14px; }
  .card--front .wordmark { top: 52px; }
  .card--back .wordmark { top: 114px; }
  .contact {
    position: absolute;
    top: 264px;
    color: var(--text-light);
  }
  .contact--person { right: 284px; text-align: right; }
  .contact__name { font-size: 20px; font-weight: 500; margin: 0 0 9px; }
  .contact__address { font-size: 15px; margin: 0; }
  .contact--lines { left: 333px; top: 266px; }
  .contact__line {
    display: flex; align-items: center; gap: 7px;
    font-size: 15px; margin: 0 0 7px;
  }
  .contact__icon { width: 12px; height: 12px; fill: var(--text-light); }
</style>
</head>
<body>
<main class="canvas">
  <section class="card card--front" aria-label="Business card front">
    <svg class="card__bands" width="588" height="363" viewBox="0 0 588 363">
      <polygon points="0,203 409,203 388,230 0,230" fill="var(--ink-black)"/>
      <polygon points="421,195 588,195 588,363 0,363 0,233 395,233" fill="var(--brand-red)"/>
    </svg>
    <div class="wordmark">
      <span class="wordmark__name">Corvane</span>
      <span class="wordmark__suffix">ELECTRONICS, INC.</span>
    </div>
    <div class="contact contact--person">
      <p class="contact__name">Paul Bredesen VP</p>
      <p class="contact__address">4518 Maple Crest Blvd. Fairhaven, TX 75098</p>
    </div>
    <div class="contact contact--lines">
      <p class="contact__line">
        <svg class="contact__icon" viewBox="0 0 24 24" aria-hidden="true"><path d="M6.6 10.8a15 15 0 0 0 6.6 6.6l2.2-2.2a1 1 0 0 1 1-.25 11.4 11.4 0 0 0 3.6.57 1 1 0 0 1 1 1V20a1 1 0 0 1-1 1A17 17 0 0 1 3 4a1 1 0 0 1 1-1h3.5a1 1 0 0 1 1 1c0 1.25.2 2.45.57 3.57a1 1 0 0 1-.25 1z"/></svg>
        214-555-0187
      </p>
      <p class="contact__line">
        <svg class="contact__icon" viewBox="0 0 24 24" aria-hidden="true"><path d="M6 2h9v5H6zM3 8h18v13H3zm3 3v2h4v-2zm0 4v2h4v-2zm7-4v6h5v-6z"/></svg>
        214-555-0143
      </p>
    </div>
  </section>

  <section class="card card--back" aria-label="Business card back">
    <div class="wordmark">
      <span class="wordmark__name">Corvane</span>
      <span class="wordmark__suffix">ELECTRONICS, INC.</span>
    </div>
  </section>
</main>
</body>
</html>
```